依頼詳細
スキンケアブランド「pluna」の洗顔スクラブのパッケージデザインをご提案いただきたく存じます。

・ターゲット:20〜30代女性
・ブランド:pluna
・商品名:Tender Skin Polish

・デザイン依頼パッケージ:チューブ・化粧箱の2種類(裏面表記なしでOK)
※チューブ/キャップ色:白 (白地チューブ×キャップにて進行)

・デザインイメージ:添付写真
・ロゴイメージ:添付写真
※ブランドロゴは記載マストでお願いいたします。
記載項目
チューブ印刷範囲、化粧箱サイズに関しては、データを添付いたします。
希望イメージ
シンプル 複雑
単色 カラフル
暗い 明るい
日常 高級
遊び心 厳粛
未来的 伝統的
女性的 男性的
希望する色
茶系、黄・オレンジ系、トーン抑えめのくすんだ茶/アプリコット/
納品ファイル
• 高解像度JPG (.jpg)
• イラストレーター形式 (.ai)
• フォトショップ形式 (.psd)
補足説明
■ 選んだ理由

大人の優雅な時間+シンプルというブランドイメージに合っていた為

■ 提案者全員のお礼・コメント

この度は沢山のご提案をいただき、誠にありがとうございました。
どのデザインもクオリティが高く、選定するのに非常に悩ましかったです。
また弊社案件がございましたら、ご提案・ご協力いただけると幸いです。
この度は、ありがとうございました。

```html
<!DOCTYPE html>
<html lang="en">
<head>
<meta charset="utf-8">
<title>pluna — Tender Skin Polish carton dieline</title>
<link href="https://fonts.googleapis.com/css2?family=Jost:wght@300;400&display=swap" rel="stylesheet">
<style>
  :root {
    --paper: #ffffff;
    --panel: #efebe5;
    --cut: #9a9a9a;
    --fold: #c4c4c4;
    --ink: #4a4541;
    --ink-soft: #8a837c;
    --art: #e4ded5;
    --label: #2d5fa8;
  }
  html, body { margin: 0; padding: 0; overflow: hidden; }
  body { width: 893px; height: 1200px; background: var(--paper); position: relative; font-family: "Jost", sans-serif; color: var(--ink); }
  .dieline { position: absolute; inset: 0; }
  .brand { position: absolute; font-weight: 300; letter-spacing: 0.42em; font-size: 20px; text-transform: lowercase; white-space: nowrap; }
  .brand--lid { left: 357px; width: 203px; top: 212px; text-align: center; font-size: 16px; }
  .brand--front { left: 351px; width: 244px; top: 420px; text-align: center; }
  .brand--side { left: 700px; top: 392px; transform: rotate(90deg); transform-origin: left top; font-size: 22px; }
  .product-name { position: absolute; left: 351px; width: 244px; top: 492px; text-align: center; font-size: 11px; letter-spacing: 0.18em; line-height: 1.35; text-transform: uppercase; }
  .claim { position: absolute; left: 351px; width: 244px; text-align: center; font-size: 6px; letter-spacing: 0.06em; line-height: 1.45; color: var(--ink-soft); }
  .claim--top { top: 530px; }
  .claim--mid { top: 558px; font-size: 6.5px; color: var(--ink); }
  .claim--net { top: 848px; }
  .artwork { position: absolute; left: 395px; top: 625px; width: 180px; height: 190px; background: radial-gradient(ellipse at 55% 40%, var(--art) 0%, var(--panel) 72%); border-radius: 4px; }
  .side-mark { position: absolute; left: 622px; top: 762px; font-size: 6px; color: var(--ink-soft); letter-spacing: 0.08em; }
  .side-note { position: absolute; left: 622px; top: 790px; width: 100px; font-size: 6px; line-height: 1.45; color: var(--ink-soft); }
  .job-label { position: absolute; left: 60px; top: 1168px; font-size: 13px; color: var(--label); letter-spacing: 0.02em; }
</style>
</head>
<body>
<svg class="dieline" width="893" height="1200" viewBox="0 0 893 1200" aria-hidden="true">
  <g fill="var(--panel)">
    <rect x="357" y="165" width="203" height="111"/>
    <rect x="113" y="276" width="625" height="624"/>
  </g>
  <g fill="none" stroke="var(--cut)" stroke-width="1">
    <!-- top tuck and lid -->
    <path d="M357 276 V165 H560 V276"/>
    <path d="M357 165 V125 Q360 105 380 105 H537 Q557 105 560 125 V165"/>
    <path d="M351 276 L300 255 V230 L320 215 H351 M595 276 L640 255 V230 L620 215 H595"/>
    <path d="M232 276 L240 255 H330 L345 276"/>
    <!-- main band outline -->
    <path d="M113 276 H738 V900 H113 Z"/>
    <path d="M113 290 L62 300 V880 L113 890"/>
    <!-- bottom flaps -->
    <path d="M113 900 L125 950 H175 L190 990 L205 950 L232 900"/>
    <path d="M232 900 V960 L260 1000 V1035 H330 L351 990 V900"/>
    <path d="M351 900 L365 960 H420 L440 1000 H510 L530 960 H580 L595 900"/>
    <path d="M595 900 L605 950 H650 L665 985 L690 950 L738 900"/>
    <!-- crop marks -->
    <path d="M20 66 H50 M60 22 V56 M873 66 H843 M833 22 V56 M20 1130 H50 M60 1160 V1140 M873 1130 H843 M833 1160 V1140"/>
    <path d="M30 300 V880 M24 300 H36 M24 880 H36"/>
  </g>
  <g fill="none" stroke="var(--fold)" stroke-width="0.8" stroke-dasharray="4 3">
    <path d="M113 276 V900 M232 276 V900 M351 276 V900 M595 276 V900"/>
    <path d="M113 276 H738 M113 900 H738 M357 165 H560"/>
  </g>
</svg>

<div class="brand brand--lid">pluna</div>

<div class="brand brand--front">pluna</div>
<div class="product-name">Tender<br>Skin Polish</div>
<div class="claim claim--top">Exfoliating &amp; softening<br>for everyday gentle care</div>
<div class="claim claim--mid">Enriched with apricot<br>and natural fine grains<br>for soft radiance</div>
<div class="artwork" role="img" aria-label="Fine line drawing of three tulip-like flowers on slender stems"></div>
<div class="claim claim--net">Net wt. 100 g<br>3.5 oz</div>

<div class="brand brand--side">pluna</div>
<div class="side-mark">pluna —</div>
<div class="side-note">Natural ingredients<br>everyday exfoliation<br>gentle on skin</div>

<div class="job-label">S0920081 211.75*150 O</div>
</body>
</html>
```